Brightwell Care Advisors, LLC Business Card update!

would like a classier business card. Our cards currently just have our logo and contact information. Need better use of color and creativity
Logo attached.

Target Market(s)

Potential clients, contacts, existing clients. We are a consulting company

Industry/Entity Type

Business

Contact Information for Business Card

We like our colors but just have a boring card with our logo and a white background. I want something that stands out.

Colors
ec1f27
757575

Requirements
Must have
• Color to stay consistent. Logo provided
Nice to have
• Just better use of color/ design

```html
<!DOCTYPE html>
<html lang="en">
<head>
<meta charset="utf-8">
<title>Brightwell Care Advisors – Business Card</title>
<link rel="stylesheet" href="https://fonts.googleapis.com/css2?family=Open+Sans:wght@400;600&display=swap">
<style>
  :root {
    --brand-red: #ec1f27;
    --brand-grey: #6a6b6c;
    --card-white: #ffffff;
    --page-bg: #e9e9e9;
    --text-light: #ffffff;
    --watermark: rgba(120, 20, 24, 0.35);
  }
  html, body {
    margin: 0;
    width: 1200px;
    height: 900px;
    overflow: hidden;
    background: var(--page-bg);
    font-family: "Open Sans", Arial, sans-serif;
  }
  .business-card {
    position: absolute;
    left: 150px;
    top: 193px;
    width: 900px;
    height: 514px;
    background: var(--card-white);
    box-shadow: 0 10px 30px rgba(0,0,0,0.18);
    overflow: hidden;
  }
  .card-bands {
    position: absolute;
    inset: 0;
    width: 900px;
    height: 514px;
  }
  .brand-lockup {
    position: absolute;
    left: 70px;
    top: 120px;
    display: flex;
    align-items: center;
    gap: 18px;
  }
  .brand-dot {
    width: 58px;
    height: 58px;
    border-radius: 50%;
    background: var(--brand-red);
    flex: none;
  }
  .brand-name {
    color: var(--brand-red);
    font-weight: 400;
    font-size: 40px;
    line-height: 1.05;
    letter-spacing: 0.5px;
  }
  .owner {
    position: absolute;
    right: 60px;
    top: 178px;
    text-align: right;
    color: var(--text-light);
  }
  .owner-name {
    font-size: 30px;
    font-weight: 600;
    letter-spacing: 0.5px;
  }
  .owner-title {
    font-size: 17px;
    font-weight: 400;
    margin-top: 2px;
  }
  .contact-list {
    position: absolute;
    left: 62px;
    top: 362px;
    margin: 0;
    padding: 0;
    list-style: none;
    color: var(--text-light);
    font-size: 20px;
    line-height: 29px;
  }
  .contact-list li {
    display: flex;
    align-items: center;
    gap: 16px;
  }
  .contact-icon {
    width: 16px;
    height: 16px;
    flex: none;
  }
  .brand-watermark {
    position: absolute;
    right: 70px;
    top: 372px;
    color: var(--watermark);
    font-size: 30px;
    font-weight: 400;
    line-height: 1.05;
  }
</style>
</head>
<body>
  <div class="business-card">
    <svg class="card-bands" viewBox="0 0 900 514" aria-hidden="true">
      <polygon points="0,268 455,268 490,160 900,160 900,310 0,310" fill="var(--brand-grey)"/>
      <rect x="0" y="310" width="900" height="204" fill="var(--brand-red)"/>
    </svg>

    <div class="brand-lockup">
      <span class="brand-dot"></span>
      <div class="brand-name">Brightwell<br>Care Advisors</div>
    </div>

    <div class="owner">
      <div class="owner-name">Owner Name</div>
      <div class="owner-title">Designation</div>
    </div>

    <ul class="contact-list">
      <li>
        <svg class="contact-icon" viewBox="0 0 16 16"><path d="M2 5c0-2 2-3 6-3s6 1 6 3v1h-3V4.5H5V6H2zM4 7h8l2 6H2z" fill="#fff"/></svg>
        (469) 123-456
      </li>
      <li>
        <svg class="contact-icon" viewBox="0 0 16 16"><rect x="4" y="1" width="8" height="5" fill="#fff"/><rect x="1" y="6" width="14" height="8" rx="1" fill="#fff"/><rect x="4" y="9" width="8" height="2" fill="var(--brand-red)"/></svg>
        (050) 123-456789
      </li>
      <li>
        <svg class="contact-icon" viewBox="0 0 16 16"><rect x="1" y="3" width="14" height="10" fill="#fff"/><path d="M1 3l7 6 7-6" fill="none" stroke="var(--brand-red)" stroke-width="1.4"/></svg>
        info@companyname.com
      </li>
      <li>
        <svg class="contact-icon" viewBox="0 0 16 16"><g fill="none" stroke="#fff" stroke-width="2"><rect x="1.5" y="6" width="7" height="4" rx="2" transform="rotate(-45 5 8)"/><rect x="7.5" y="6" width="7" height="4" rx="2" transform="rotate(-45 11 8)"/></g></svg>
        www.companyname.com
      </li>
    </ul>

    <div class="brand-watermark">Brightwell<br>Care Advisors</div>
  </div>
</body>
</html>
```